New Brochure Design Project *

I am in need of a brochure design/layout that 'Wows' prospective customers and provides essential information about our company.
The name of the Company is Tessa Wren Charter Fishing Service.
Located in Port Washington, Wisconsin.
We take customers fishing on Lake Michigan . We have been in business for over 30 years with a reputation for the most successful fishing charter in the area. Voted best fishing Charter for several years in a row. We fish for Chinook Salmon, Steelhead, Brown Trout, Coho Salmon and Lake Trout. Our fleet of 4 large fishing boats are well maintained and fully equipped with all fishing tackle , the latest in fishing gear and electronics, private restroom, heat and air. Fully insured. Our boats are U.S. Coast Guard Certified and licensed to accommodate 1 to 6 passengers.
Our selected Captains have over 100 years of experience fishing Lake Michigan .
Target market: Corporations that provide team building exercises,/ rewards employees for a job well done/ entertain clients, Outdoor enthusiasts, Men, women and families that enjoy fresh water fishing.
Design specifics: I would like to have 5-7 photos of our catch, ( I can provide those ) photos of the 4 boats ( I will provide ) Our Logo ( I will provide ) A page for our rates and packages, our website, contact information.
Our current brochure can be viewed on our website under the downloadable brochure tab. At www.tessawrencharters-example.com Our Facebook www.facebook-example.com/TessaWrenChartersLLC page is a great way to learn more about us as well and responses from our customers plus reviews of our Company for reference. I am open to advice on this project.
Our current brochure is a colored two sided brochure with 5 panels that fold up ( almost accordion style ) with a front and back cover. I am open to new layouts and easier folding options.
Attached is our logo, and current brochure. I will send photos as needed.( I will be making price adjustments for the new brochure)
Thank you so much for your help.

```html
<!DOCTYPE html>
<html lang="en">
<head>
<meta charset="utf-8">
<title>Tessa Wren Charter Fishing Service – Rates &amp; Packages</title>
<link rel="stylesheet" href="https://fonts.googleapis.com/css2?family=Lobster&family=PT+Sans:wght@400;700&family=Roboto+Condensed:wght@700&family=Oswald:wght@500&display=swap">
<style>
  :root{
    --green:#7db43a;
    --deposit:#a6d04a;
    --blue-deep:#0b3f86;
    --blue-mid:#1460b0;
    --blue-light:#2b86d1;
    --ink:#3a3a3a;
    --white:#ffffff;
  }
  *{margin:0;padding:0;box-sizing:border-box}
  html,body{width:1200px;height:934px;overflow:hidden;background:#fff}
  .brochure{position:relative;width:1200px;height:934px;overflow:hidden;font-family:"PT Sans",sans-serif;color:var(--ink)}

  /* left panel */
  .info-panel{position:absolute;left:0;top:0;width:402px;height:934px;background:var(--white)}
  .info-title{position:absolute;left:33px;top:34px;font-family:"Lobster",cursive;font-size:22px;color:var(--green);font-weight:400}
  .info-text{position:absolute;left:33px;width:340px;font-size:14.5px;line-height:19px}
  .intro{top:78px}
  .fleet-grid{position:absolute;left:33px;top:152px;width:341px;display:grid;grid-template-columns:164px 164px;gap:10px 13px}
  .boat-photo{height:96px;background:linear-gradient(180deg,#a9c6dc 0%,#d6e2ea 30%,#f4f6f7 48%,#8aa4b6 62%,#2f6b95 82%,#24577d 100%)}
  .fleet-heading{position:absolute;left:33px;top:378px;font-size:15px;font-weight:700;color:var(--green)}
  .fleet-list{position:absolute;left:33px;top:398px;list-style:none;font-size:14.5px;line-height:19.5px}
  .fleet-list li::before{content:"• "}
  .fleet-note{top:499px;text-align:justify}
  .dock-photo{position:absolute;left:0;top:620px;width:402px;height:314px}

  /* right area */
  .rates-area{position:absolute;left:402px;top:0;width:798px;height:934px;
    background:radial-gradient(ellipse at 60% 55%,var(--blue-light) 0%,var(--blue-mid) 45%,var(--blue-deep) 100%)}
  .crew-photo{position:absolute;left:0;top:0;width:798px;height:400px}
  .catch-circle{position:absolute;border-radius:50%;border:4px solid var(--white)}
  .catch-one{left:425px;top:258px;width:120px;height:120px;
    background:linear-gradient(180deg,#c8d8e4 0%,#9fb7c8 30%,#3c4750 55%,#5b6a74 75%,#2e5f86 100%)}
  .catch-two{left:578px;top:224px;width:144px;height:144px;
    background:linear-gradient(180deg,#cfdde8 0%,#aec4d4 28%,#4d5f6c 50%,#2f66a3 72%,#27507a 100%)}

  .rates-title{position:absolute;left:47px;top:412px;font-family:"Lobster",cursive;font-size:29px;color:var(--white);font-weight:400}
  .package{position:absolute;color:var(--white);font-size:14.5px;line-height:20.6px}
  .package-banner{position:relative;height:30px;margin-bottom:8px}
  .package-banner svg{position:absolute;left:0;top:0}
  .package-banner h3{position:relative;font-family:"Roboto Condensed",sans-serif;font-size:16px;font-weight:700;
    color:var(--white);text-align:center;line-height:30px;text-transform:uppercase;letter-spacing:.2px}
  .deposit{color:var(--deposit);font-weight:700}
  .fisherman{left:27px;top:464px;width:300px}
  .chinook{left:415px;top:464px;width:280px;line-height:17px}
  .chinook .package-banner{margin-bottom:10px}
  .captain{left:27px;top:654px;width:300px}
  .halfday{left:415px;top:654px;width:280px}
  .rate-row{display:flex;width:195px}
  .rate-row .dots{flex:1;border-bottom:1.5px dotted var(--white);margin:0 3px 5px}
  .fine-print{position:absolute;left:415px;top:812px;width:364px;font-size:10.3px;line-height:13.6px;color:var(--white);text-align:justify}
  .call-line{position:absolute;left:39px;top:876px;display:flex;align-items:center;gap:6px;
    font-family:"Oswald",sans-serif;font-size:23px;color:var(--deposit);letter-spacing:.3px}
</style>
</head>
<body>
<div class="brochure">

  <section class="info-panel">
    <h1 class="info-title">The Finest Fishing on Lake Michigan!</h1>
    <p class="info-text intro">The key to a successful fishing trip starts with our professional Captains with over 100 years of combined experience fishing Lake Michigan.</p>

    <div class="fleet-grid">
      <div class="boat-photo" role="img" aria-label="Photo of the Tessa Wren charter boat at the dock"></div>
      <div class="boat-photo" role="img" aria-label="Photo of the stern of Tessa Wren II"></div>
      <div class="boat-photo" role="img" aria-label="Photo of Tessa Wren III on the water"></div>
      <div class="boat-photo" role="img" aria-label="Photo of Tessa Wren IV on the water"></div>
    </div>

    <h2 class="fleet-heading">Size does matter when fishing Lake Michigan!</h2>
    <ul class="fleet-list">
      <li>Tessa Wren- 35ft extra wide Norvik</li>
      <li>Tessa Wren II - 34ft Keelmark Sport Fisherman</li>
      <li>Tessa Wren III - 36ft extra wide Corvale</li>
      <li>Tessa Wren IV - 36ft extra wide Corvale</li>
    </ul>

    <p class="info-text fleet-note">All of our boats are US Coast Guard certified and licensed to accommodate 1-6 passengers. Our fleet offers all fishing tackle needed, the latest in fishing gear and electronics, private restroom, heat, and air conditioning. All of our boats are fully insured</p>

    <svg class="dock-photo" viewBox="0 0 402 314" role="img" aria-label="Photo of a large group of anglers on the dock behind their catch of salmon and trout">
      <defs>
        <linearGradient id="dockTones" x1="0" y1="0" x2="0" y2="1">
          <stop offset="0" stop-color="#d2dde4"/>
          <stop offset=".22" stop-color="#9aa9b2"/>
          <stop offset=".38" stop-color="#3e4246"/>
          <stop offset=".58" stop-color="#4c5258"/>
          <stop offset=".72" stop-color="#b9bec2"/>
          <stop offset="1" stop-color="#8b8f8c"/>
        </linearGradient>
      </defs>
      <path d="M0 30 Q200 -10 402 22 V314 H0Z" fill="url(#dockTones)"/>
      <path d="M0 22 Q200 -18 402 14 V24 Q200 -6 0 36Z" fill="#1a63b3"/>
      <path d="M0 12 Q200 -26 402 4 V14 Q200 -16 0 24Z" fill="#7db43a"/>
    </svg>
  </section>

  <section class="rates-area">
    <svg class="crew-photo" viewBox="0 0 798 400" role="img" aria-label="Photo of six smiling anglers giving thumbs up on the boat deck with their salmon catch">
      <defs>
        <linearGradient id="crewTones" x1="0" y1="0" x2="0" y2="1">
          <stop offset="0" stop-color="#c9d6de"/>
          <stop offset=".2" stop-color="#a9b8c2"/>
          <stop offset=".38" stop-color="#3a4450"/>
          <stop offset=".6" stop-color="#4a5968"/>
          <stop offset=".75" stop-color="#c6ccd0"/>
          <stop offset="1" stop-color="#e2e5e5"/>
        </linearGradient>
        <linearGradient id="crewColour" x1="0" y1="0" x2="1" y2="0">
          <stop offset="0" stop-color="#2d3a46" stop-opacity=".35"/>
          <stop offset=".3" stop-color="#e0c23a" stop-opacity=".28"/>
          <stop offset=".5" stop-color="#2f6fc0" stop-opacity=".3"/>
          <stop offset=".72" stop-color="#c0302e" stop-opacity=".3"/>
          <stop offset="1" stop-color="#9aa3ab" stop-opacity=".25"/>
        </linearGradient>
      </defs>
      <path d="M0 0 H798 V300 Q560 360 300 355 Q120 352 0 372Z" fill="url(#crewTones)"/>
      <path d="M0 0 H798 V300 Q560 360 300 355 Q120 352 0 372Z" fill="url(#crewColour)"/>
      <path d="M0 372 Q120 352 300 355 Q560 360 798 300 V312 Q560 372 300 368 Q130 365 0 392Z" fill="#7db43a"/>
    </svg>
    <div class="catch-circle catch-one" role="img" aria-label="Photo of an angler holding two large salmon"></div>
    <div class="catch-circle catch-two" role="img" aria-label="Photo of a young angler with a row of hanging trout"></div>

    <h2 class="rates-title">Rates &amp; Packages</h2>

    <article class="package fisherman">
      <div class="package-banner">
        <svg width="282" height="30" viewBox="0 0 282 30"><path d="M4 3 L276 1 L281 8 L274 15 L280 24 L270 29 L8 28 L1 22 L6 14 L0 6Z" fill="var(--green)"/></svg>
        <h3>Fisherman's Special</h3>
      </div>
      <p>3- five hour charters<br>2 nights lodging<br>All licenses and Trout stamps ( Two day only )<br>3 people $690.pp / 4 people $520.pp<br>5 people $472.pp/ 6 people $395.pp<br><span class="deposit">Deposit of $600 required.</span></p>
    </article>

    <article class="package chinook">
      <div class="package-banner">
        <svg width="258" height="30" viewBox="0 0 258 30"><path d="M4 3 L252 1 L257 8 L250 15 L256 24 L246 29 L8 28 L1 22 L6 14 L0 6Z" fill="var(--green)"/></svg>
        <h3>Chinook &amp; Coho Special</h3>
      </div>
      <p>2- five hour charters<br>Five hours afternoon<br>Five hours morning<br>All licenses and Trout stamps<br>One night lodging<br>3 people $450. pp/ 4 people $340.pp<br>5 people $302.pp / 6 people $254.pp<br><span class="deposit">Deposit of $300 required.</span></p>
    </article>

    <article class="package captain">
      <div class="package-banner">
        <svg width="282" height="30" viewBox="0 0 282 30"><path d="M4 3 L276 1 L281 8 L274 15 L280 24 L270 29 L8 28 L1 22 L6 14 L0 6Z" fill="var(--green)"/></svg>
        <h3>Captain's Special</h3>
      </div>
      <p>2- six hour charters<br>Six hours afternoon<br>Six hours morning<br>All licenses and Trout stamps<br>One night lodging<br>3 people $504.pp/ 4 people $380.pp<br>5 people $334.pp/ 6 people $280.pp<br><span class="deposit">Deposit of $400 required.</span></p>
    </article>

    <article class="package halfday">
      <div class="package-banner">
        <svg width="258" height="30" viewBox="0 0 258 30"><path d="M4 3 L252 1 L257 8 L250 15 L256 24 L246 29 L8 28 L1 22 L6 14 L0 6Z" fill="var(--green)"/></svg>
        <h3>Half Day Rates</h3>
      </div>
      <p>(up to 6 persons maximum)</p>
      <div class="rate-row"><span>5 Hours</span><span class="dots"></span><span>$590</span></div>
      <div class="rate-row"><span>6 Hours</span><span class="dots"></span><span>$670</span></div>
      <div class="rate-row"><span>7 Hours</span><span class="dots"></span><span>$750</span></div>
      <p class="deposit">Deposit of $250 required.</p>
    </article>

    <p class="fine-print">Package pricing is based on accommodations at Harbor Rest Inn &amp; Suites Port Washington. 1-4 persons 1 room / 4-6 persons 2 rooms. In the event your Captain determines the weather conditions are unsafe for your trip, your charter will be rescheduled at no additional cost. A 3% convenience fee will be added for payments by credit card. Deposits are non refundable 30 days prior to your reservation date.</p>

    <p class="call-line">CALL US TODAY
      <svg width="22" height="22" viewBox="0 0 24 24" aria-hidden="true"><circle cx="12" cy="12" r="10.5" fill="none" stroke="var(--deposit)" stroke-width="2"/><path d="M8.2 6.5l1.8-.4 1.2 2.8-1.2 1a7 7 0 0 0 3.6 3.6l1-1.2 2.8 1.2-.4 1.8c-.2.6-.8 1-1.4 1A9.5 9.5 0 0 1 7.2 7.9c0-.6.4-1.2 1-1.4z" fill="var(--deposit)"/></svg>
      1-877-555-0142</p>
  </section>

</div>
</body>
</html>
```